Business Card Design Project used as hotel key

I need a project to be printed on PVC card and used by our customers as room key.

The design and the color are up to you. My idea would be to include the logo (colour can also be changed) on the front side and our Internet address on the back (http://www.valmirenza.ch, info@valmirenza.ch).

Target Market(s)

Hôtel customers

Industry/Entity Type

Hotel

Requirements
Must have
• I have attached below the template of the front and back of the card. The logo on the back shown on the template below the magnetic stripe should not be used.

Must have:

1. Follow the template size (shown in the template):

Full Bleed Size:
3.55" x 2.3"
90.17mm x 58.42mm
1065 x 690 pixels

Trim Size:
3.375" x 2.125"
85.77mm x 54.02mm
1013 x 638 pixels

A bleed is the outer area of your artwork that falls on the outside of the trim line. It is important that you do not have any important information in the bleed area as ¼ “ will be cut off on all sides. Cards with a “framed border” are not recommended due to variances in die cutting.

2. Make sure you leave the area between the magstripe markers on the template blank.

3. There need to be an arrow on the front side (on the left), pointing the left side

4. Color: Full color both sides, color process CMYK. 300 DPI at 100% of the final print size

```html
<!DOCTYPE html>
<html lang="en">
<head>
<meta charset="utf-8">
<title>Hôtel Valmirenza – Key Card</title>
<link rel="stylesheet" href="https://fonts.googleapis.com/css2?family=Jost:wght@400;500;600&display=swap">
<style>
  :root {
    --page-bg: #ece8e6;
    --front-dark: #21131f;
    --front-mid: #3d2a3b;
    --mauve: #8b5866;
    --mauve-text: #8e5a66;
    --back-bg: #ffffff;
    --ink: #2b2b2b;
    --guide-tone: #f1ecee;
  }
  * { box-sizing: border-box; margin: 0; padding: 0; }
  html, body {
    width: 1200px; height: 778px; overflow: hidden;
    background: var(--page-bg);
    font-family: "Jost", "Century Gothic", sans-serif;
  }
  .sheet {
    position: relative; width: 1200px; height: 778px;
    display: flex; align-items: center; justify-content: center; gap: 32px;
  }
  .card {
    position: relative; width: 560px; height: 353px;
    border-radius: 14px; overflow: hidden;
    box-shadow: 0 6px 18px rgba(0,0,0,.18);
  }
  /* front */
  .card--front {
    background: radial-gradient(ellipse at 35% 40%, var(--front-mid) 0%, var(--front-dark) 85%);
    display: flex; align-items: center; justify-content: center;
    padding-left: 40px;
  }
  .wordmark {
    display: flex; align-items: center; gap: 12px;
    color: var(--mauve-text); font-weight: 600;
    text-transform: uppercase; letter-spacing: 2px;
  }
  .wordmark__dot {
    flex: none; width: 16px; height: 16px; border-radius: 50%; background: var(--mauve-text);
  }
  .wordmark__name { font-size: 34px; line-height: 1; white-space: nowrap; }
  .key-arrow { position: absolute; left: 22px; top: 50%; transform: translateY(-50%); }
  /* back */
  .card--back { background: var(--back-bg); }
  .magstripe {
    position: absolute; left: 0; right: 0; top: 42px; height: 64px;
    background: var(--mauve);
    display: flex; align-items: center; justify-content: flex-end; padding-right: 40px;
  }
  .magstripe__label {
    font-size: 27px; font-weight: 500; letter-spacing: 3px; color: #111;
  }
  .usage-guide {
    position: absolute; left: 36px; top: 118px; width: 400px; height: 120px;
    background: linear-gradient(180deg, var(--guide-tone), #fafafa);
    border-radius: 6px;
  }
  .steps {
    position: absolute; left: 38px; top: 250px;
    display: flex; flex-direction: column; gap: 2px;
    font-size: 15px; color: var(--ink); line-height: 1.35;
  }
  .steps__row { display: flex; gap: 18px; list-style: none; }
  .steps__item { display: inline-flex; align-items: center; gap: 7px; white-space: nowrap; }
  .steps__item::before {
    content: ""; flex: none; width: 6px; height: 6px; border-radius: 50%;
    background: var(--mauve);
  }
  .contact {
    position: absolute; left: 38px; top: 310px;
    display: flex; gap: 22px; font-size: 15px; color: var(--ink);
  }
  .contact__item { display: flex; align-items: center; gap: 6px; }
</style>
</head>
<body>
<main class="sheet">
  <section class="card card--front" aria-label="Key card front">
    <svg class="key-arrow" width="34" height="24" viewBox="0 0 34 24" aria-hidden="true">
      <path d="M32 12H6M14 3L4 12l10 9" fill="none" stroke="var(--mauve)" stroke-width="3" stroke-linecap="round" stroke-linejoin="round"/>
    </svg>
    <div class="wordmark">
      <span class="wordmark__dot"></span>
      <span class="wordmark__name">Hôtel Valmirenza</span>
    </div>
  </section>

  <section class="card card--back" aria-label="Key card back">
    <div class="magstripe"><span class="magstripe__label">MAGNETIC STRIPE</span></div>
    <div class="usage-guide" role="img" aria-label="Line pictograms showing how to insert the keycard, open the door handle and remove the card"></div>
    <div class="steps">
      <ul class="steps__row">
        <li class="steps__item">Fully insert or swipe Keycard</li>
        <li class="steps__item">Remove Keycard</li>
      </ul>
      <ul class="steps__row">
        <li class="steps__item">Depress handle and open door</li>
      </ul>
    </div>
    <div class="contact">
      <span class="contact__item">
        <svg width="12" height="12" viewBox="0 0 12 12" aria-hidden="true"><circle cx="6" cy="6" r="5" fill="none" stroke="var(--mauve)" stroke-width="1.5"/><path d="M1 6h10M6 1c2 2.5 2 7.5 0 10M6 1c-2 2.5-2 7.5 0 10" fill="none" stroke="var(--mauve)" stroke-width="1"/></svg>
        www.valmirenza.ch
      </span>
      <span class="contact__item">
        <svg width="13" height="10" viewBox="0 0 13 10" aria-hidden="true"><rect x="0.5" y="0.5" width="12" height="9" rx="1" fill="var(--mauve)"/><path d="M1 1l5.5 4.5L12 1" fill="none" stroke="#fff" stroke-width="1"/></svg>
        info@valmirenza.ch
      </span>
    </div>
  </section>
</main>
</body>
</html>
```